Veterinary Clinic Letterhead - Ridgeview Veterinary Surgery

We need a letterhead design for an established Veterinary Clinic in Mareeba called Ridgeview Veterinary Surgery. We are a moderate sized mixed animal veterinary clinic offering a wide variety of veterinary services. The design should use the same colour pattern as those in the logos supplied. The design should also include our address (48 Tulloch Road, Ashvale, Northvale, 5127), phone number (07 4158 6734), email (admin@ridgeviewvets.com.au), website (www.ridgeviewvets.com.au) and our opening hours (7:30am to 6pm Monday to Friday and 9am to 1pm Saturday).
Target Market(s)
Pet owners
Industry/Entity Type
Veterinary
Requirements
Must have
- The logo or modification of it, business address, opening hours, website, phone number and email address

```html
<!DOCTYPE html>
<html lang="en">
<head>
<meta charset="utf-8">
<title>Ridgeview Veterinary Surgery – Letterhead</title>
<link href="https://fonts.googleapis.com/css2?family=Open+Sans:wght@400;600;700&family=Raleway:wght@400;700&display=swap" rel="stylesheet">
<style>
  :root {
    --navy: #13294b;
    --ink: #2f3238;
    --body: #8a8d93;
    --muted: #7d8086;
    --rule: #6b6f78;
    --paper: #ffffff;
    --signature-tone: #d6d8dc;
  }
  * { box-sizing: border-box; margin: 0; padding: 0; }
  html, body { width: 968px; height: 1200px; overflow: hidden; background: var(--paper); }
  .letterhead {
    position: relative;
    width: 968px; height: 1200px;
    background: var(--paper);
    font-family: "Open Sans", Arial, sans-serif;
    color: var(--ink);
  }
  .brand {
    position: absolute; left: 0; right: 0; top: 28px;
    display: flex; flex-direction: column; align-items: center;
  }
  .brand-mark { width: 108px; height: 108px; }
  .brand-name {
    margin-top: 6px;
    font-weight: 600;
    font-size: 19px;
    letter-spacing: 1.5px;
    text-transform: uppercase;
    color: var(--navy);
  }
  .header-rule {
    position: absolute; left: 0; right: 0; top: 172px;
    height: 1.5px; background: var(--navy);
  }
  .recipient { position: absolute; left: 77px; top: 318px; }
  .recipient-name { font-size: 20px; font-weight: 700; color: var(--ink); line-height: 26px; }
  .recipient-role { margin-top: 2px; font-size: 13px; color: var(--muted); }
  .letter-date {
    position: absolute; right: 77px; top: 362px;
    font-size: 13px; color: var(--ink);
  }
  .letter-body {
    position: absolute; left: 77px; top: 410px; width: 814px;
  }
  .letter-body p {
    font-size: 13px; line-height: 18px;
    color: var(--body); text-align: justify;
    margin-bottom: 18px;
  }
  .sign-off { position: absolute; left: 77px; top: 864px; }
  .signature {
    width: 150px; height: 30px;
    background: linear-gradient(90deg, var(--signature-tone), #eceef0);
    border-radius: 3px;
  }
  .signer-name { margin-top: 8px; font-size: 18px; font-weight: 600; text-transform: uppercase; color: var(--ink); line-height: 24px; }
  .signer-role { margin-top: 1px; font-size: 13px; color: var(--muted); }
  .contact {
    position: absolute; top: 1082px; left: 0; right: 0;
    font-family: "Raleway", Arial, sans-serif;
    font-size: 15px; color: var(--muted);
  }
  .contact-col { position: absolute; display: flex; flex-direction: column; gap: 4px; }
  .contact-col.left { left: 187px; }
  .contact-col.right { left: 441px; }
  .contact-divider { position: absolute; left: 422px; top: 0; width: 1px; height: 42px; background: var(--rule); }
  .contact-item { display: flex; align-items: center; gap: 5px; line-height: 18px; }
  .contact-item svg { width: 11px; height: 11px; flex: none; }
  .hours {
    position: absolute; left: 115px; width: 738px; top: 1139px; height: 30px;
    border-top: 1px solid var(--rule); border-bottom: 1px solid var(--rule);
    display: flex; align-items: center; justify-content: center;
    font-family: "Raleway", Arial, sans-serif; font-size: 15px; color: var(--muted);
  }
  .hours strong { color: var(--navy); font-weight: 700; margin-right: 4px; }
</style>
</head>
<body>
<main class="letterhead">
  <header class="brand">
    <svg class="brand-mark" viewBox="0 0 100 100" aria-hidden="true">
      <circle cx="50" cy="50" r="44" fill="none" stroke="var(--navy)" stroke-width="7"/>
    </svg>
    <div class="brand-name">Ridgeview Veterinary Surgery</div>
  </header>
  <div class="header-rule"></div>

  <section class="recipient">
    <div class="recipient-name">Name Surname</div>
    <div class="recipient-role">Senior Executive</div>
  </section>
  <div class="letter-date">Date, 10 September, 2030</div>

  <section class="letter-body">
    <p>Lorem ipsum dolor sit amet, consectetur adipisicing elit, sed do eiusmod tempor incididunt ut labore et dolore magna aliqua. Ut enim ad minim veniam, quis nostrud exercitation ullamco laboris nisi ut aliquip ex ea commodo consequat. Duis aute irure dolor in reprehenderit in voluptate velit esse cillum dolore eu fugiat nulla pariatur. Excepteur sint occaecat cupidatat non proident, sunt in culpa qui officia deserunt mollit anim id est laborum. Sed ut perspiciatis unde omnis iste natus error sit voluptatem accusantium doloremque laudantium, totam rem aperiam, eaque ipsa quae ab illo inventore veritatis et quasi architecto beatae vitae dicta sunt explicabo. Nemo enim ipsam voluptatem quia voluptas sit aspernatur aut odit aut fugit, sed quia consequuntur magni dolores eos qui ratione voluptatem sequi nesciunt. Neque porro voluptatem sequi nesciunt. Nemo enim ipsam voluptatem quia voluptas.</p>
    <p>Lorem ipsum dolor sit amet, consectetur adipisicing elit, sed do eiusmod tempor incididunt ut labore et dolore magna aliqua. Ut enim ad minim veniam, quis nostrud exercitation ullamco laboris nisi ut aliquip ex ea commodo consequat. Duis aute irure dolor in reprehenderit in voluptate velit esse cillum dolore eu fugiat nulla pariatur. Excepteur sint occaecat cupidatat non proident, sunt in culpa qui officia deserunt mollit anim id est laborum. Sed ut perspiciatis unde omnis iste natus error sit voluptatem accusantium doloremque laudantium, totam rem aperiam, eaque ipsa quae ab illo inventore veritatis et quasi architecto beatae vitae dicta sunt explicabo. Nemo enim ipsam voluptatem quia voluptas sit aspernatur aut odit aut.</p>
    <p>Lorem ipsum dolor sit amet, consectetur adipisicing elit, sed do eiusmod tempor incididunt ut labore et dolore magna aliqua. Ut enim ad minim veniam, quis nostrud exercitation ullamco laboris nisi ut aliquip ex ea commodo consequat.ua. Ut enim ad minim veniam, quis nostrud exercitation ullamco laboris nisi ut aliquip ex ea commodo consequat. Duis aute irure dolor in reprehenderit in voluptate velit esse cillum dolore eu fugiat nulla pariatur. Excepteur sint occaecat cupidatat non proident, sunt in culpa qui officia deserunt mollit anim id est laborum. Sed ut perspiciatis unde omnis iste natus error sit voluptatem accusantium doloremque laudantium, totam rem aperiam, eaque ipsa quae ab illo inventore veritatis et quasi architecto beatae vitae dicta sunt explicabo. Nemo enim ipsam voluptatem</p>
  </section>

  <section class="sign-off">
    <div class="signature" role="img" aria-label="Handwritten signature of the general manager"></div>
    <div class="signer-name">Name Surname</div>
    <div class="signer-role">General Manager</div>
  </section>

  <footer>
    <div class="contact">
      <div class="contact-col left">
        <div class="contact-item">
          <svg viewBox="0 0 10 10" aria-hidden="true"><circle cx="5" cy="5" r="5" fill="var(--navy)"/><path d="M3.3 2.6l1 1-.5.6c.4.8 1 1.4 1.8 1.8l.6-.5 1 1-.7.8C4.8 7 3 5.2 2.6 3.3z" fill="#fff"/></svg>
          <span>07 4158 6734</span>
        </div>
        <div class="contact-item">
          <svg viewBox="0 0 10 10" aria-hidden="true"><circle cx="5" cy="5" r="5" fill="var(--navy)"/><rect x="2.5" y="3.3" width="5" height="3.4" fill="none" stroke="#fff" stroke-width=".8"/><path d="M2.5 3.3L5 5.3l2.5-2" fill="none" stroke="#fff" stroke-width=".8"/></svg>
          <span>admin@ridgeviewvets.com.au</span>
        </div>
      </div>
      <div class="contact-divider"></div>
      <div class="contact-col right">
        <div class="contact-item">
          <svg viewBox="0 0 10 10" aria-hidden="true"><circle cx="5" cy="5" r="4.4" fill="none" stroke="var(--navy)" stroke-width="1"/><ellipse cx="5" cy="5" rx="2" ry="4.4" fill="none" stroke="var(--navy)" stroke-width=".8"/><path d="M.6 5h8.8M1.3 3h7.4M1.3 7h7.4" stroke="var(--navy)" stroke-width=".7"/></svg>
          <span>www.ridgeviewvets.com.au</span>
        </div>
        <div class="contact-item">
          <svg viewBox="0 0 10 10" aria-hidden="true"><circle cx="5" cy="5" r="5" fill="var(--navy)"/><path d="M5 2.2a1.9 1.9 0 0 1 1.9 1.9C6.9 5.4 5 7.8 5 7.8S3.1 5.4 3.1 4.1A1.9 1.9 0 0 1 5 2.2z" fill="#fff"/><circle cx="5" cy="4.1" r=".7" fill="var(--navy)"/></svg>
          <span>48 Tulloch Road, Ashvale, Northvale, 5127</span>
        </div>
      </div>
    </div>
    <div class="hours"><strong>OPENING HOURS</strong>(7:30am to 6pm Monday to Friday and 9am to 1pm Saturday).</div>
  </footer>
</main>
</body>
</html>
```